Business Card: RW Office Partners - Your tidy answer finder

Business Name: RW Office Partners
Website: www.rwofficepartners.com.au
Email: marisol@rwofficepartners.com.au
Mobile: 61 487 902 346
Facebook: @rwofficepartners
Instrgram: @rwofficepartners

Brading Colours:
HEX
#986474
#ddccd3
#7a8498
#c9d8e4
#000000
#ffffff

Tag Line: Your organised problem solver

Link to DRAFT website:
https://helpdeskhub.sitebuilderx.com/rw-office-partners

About Page from the website:
My name is Marisol Bramwell, and I would love to assist you to become more productive in your day to day and achieve your business and personal goals.
My mission is to give you time, time to work on the important tasks of your business or to be able to spend more time with your family. I will take on the tasks you don’t have time for, don’t know well or simply don’t like to do.
I have an extensive background in Administration, Tender Coordination, Document Control, WHS and Quality Management working primarily in the Construction, Mining and Corporate World.
I am passionate about being organised, having order and making things in your life (and mine) easier! I love to watch something unfold and grow into something amazing! I am known for being the go-to problem solver, the organiser of all things, producing high standards of work even under pressure. I’m also a confident communicator, and I understand that you’re busy running your business.

Target Market(s)

Small to Medium Business who require assistance in their business by a virtual assistant.

Industry/Entity Type

Virtual Assistant

Contact Information for Business Card

Mobile: 61 487 902 346

Font styles to use
Sans Serif

Colors
ffffff

Requirements
Must have
• Branding Colours as outlined.
Contact Details as outlined.
Logo as provided.
Proper contact details - mobile, facebook, instragm, website.
Simple, Elegant, very clean looking.
Should not have
• Note cute with pictures.
Not too girly as still want to market to construction companies.

```html
<!DOCTYPE html>
<html lang="en">
<head>
<meta charset="utf-8">
<title>RW Office Partners – Business Card</title>
<link rel="stylesheet" href="https://fonts.googleapis.com/css2?family=Montserrat:wght@400;500;600&display=swap">
<style>
  :root {
    --plum: #986474;
    --plum-soft: #ddccd3;
    --slate: #7a8498;
    --mist: #c9d8e4;
    --ink: #000000;
    --paper: #ffffff;
    --stage: #eeeef0;
  }
  * { margin: 0; padding: 0; box-sizing: border-box; }
  html, body { width: 1200px; height: 900px; overflow: hidden; }
  body {
    background: var(--stage);
    font-family: "Montserrat", Arial, sans-serif;
    position: relative;
  }
  .card {
    position: absolute;
    width: 560px;
    height: 320px;
    background: var(--paper);
    box-shadow: 0 6px 18px rgba(0,0,0,0.12);
    overflow: hidden;
  }
  .card--front { left: 320px; top: 60px; }
  .card--back  { left: 320px; top: 500px; }
  .card-art { position: absolute; inset: 0; width: 100%; height: 100%; }

  /* Front */
  .brand {
    position: absolute;
    display: flex;
    align-items: center;
    gap: 10px;
  }
  .brand-mark { width: 14px; height: 14px; background: var(--plum); flex: none; }
  .brand-name {
    font-weight: 600;
    letter-spacing: 1.5px;
    text-transform: uppercase;
  }
  .card--front .brand { left: 70px; top: 108px; }
  .card--front .brand-name { font-size: 24px; color: var(--slate); }
  .tagline {
    position: absolute;
    left: 94px; top: 146px;
    font-size: 10.5px;
    font-weight: 600;
    letter-spacing: 1.2px;
    text-transform: uppercase;
    color: var(--slate);
  }
  .front-web {
    position: absolute;
    left: 310px; top: 264px;
    font-size: 13px;
    letter-spacing: 0.5px;
    color: var(--plum-soft);
  }

  /* Back */
  .card--back .brand { left: 392px; top: 40px; align-items: flex-start; }
  .card--back .brand-mark { background: var(--paper); margin-top: 4px; }
  .card--back .brand-name {
    font-size: 17px;
    line-height: 1.3;
    color: var(--paper);
    width: 130px;
  }
  .contact-list { position: absolute; left: 0; top: 44px; list-style: none; }
  .contact-item {
    display: flex;
    align-items: center;
    height: 34px;
    margin-bottom: 14px;
    font-size: 13px;
    color: #333;
  }
  .contact-tab {
    width: 44px; height: 34px;
    background: var(--plum);
    display: flex; align-items: center; justify-content: center;
    margin-right: 14px;
  }
  .contact-tab svg { width: 18px; height: 18px; }
  .social-row {
    position: absolute;
    left: 58px; bottom: 28px;
    display: flex; gap: 28px;
    font-size: 11px; color: #444;
  }
  .social-item { display: flex; align-items: center; gap: 6px; }
  .social-dot { width: 9px; height: 9px; border-radius: 50%; background: var(--slate); }
</style>
</head>
<body>

<section class="card card--front" aria-label="Card front">
  <svg class="card-art" viewBox="0 0 560 320" preserveAspectRatio="none">
    <defs>
      <linearGradient id="patternTone" x1="0" y1="0" x2="1" y2="1">
        <stop offset="0" stop-color="#f3f6f9"/>
        <stop offset="1" stop-color="#e6edf3"/>
      </linearGradient>
    </defs>
    <rect width="560" height="320" fill="url(#patternTone)" role="img" aria-label="Faint repeating brand-letter pattern"/>
    <path d="M40,320 Q330,300 530,0 L560,0 L560,320 Z" fill="var(--slate)"/>
    <path d="M70,320 Q350,300 560,26 L560,320 Z" fill="var(--plum)"/>
  </svg>
  <div class="brand">
    <span class="brand-mark"></span>
    <span class="brand-name">RW Office Partners</span>
  </div>
  <p class="tagline">Your tidy answer finder</p>
  <p class="front-web">www.rwofficepartners.com.au</p>
</section>

<section class="card card--back" aria-label="Card back">
  <svg class="card-art" viewBox="0 0 560 320" preserveAspectRatio="none">
    <rect width="560" height="320" fill="var(--plum)"/>
    <path d="M0,0 H300 Q400,160 360,320 H0 Z" fill="var(--slate)"/>
    <path d="M0,0 H292 Q390,160 348,320 H0 Z" fill="var(--paper)"/>
  </svg>
  <div class="brand">
    <span class="brand-mark"></span>
    <span class="brand-name">RW Office Partners</span>
  </div>
  <ul class="contact-list">
    <li class="contact-item">
      <span class="contact-tab">
        <svg viewBox="0 0 18 18" fill="none" stroke="#fff" stroke-width="1.5"><rect x="2" y="4" width="14" height="10"/><path d="M2,4 L9,10 L16,4"/></svg>
      </span>
      marisol@rwofficepartners.com.au
    </li>
    <li class="contact-item">
      <span class="contact-tab">
        <svg viewBox="0 0 18 18" fill="none" stroke="#fff" stroke-width="1.5"><rect x="5" y="2" width="8" height="14" rx="1.5"/><path d="M8,13.5 H10"/></svg>
      </span>
      61 487 902 346
    </li>
    <li class="contact-item">
      <span class="contact-tab">
        <svg viewBox="0 0 18 18" fill="none" stroke="#fff" stroke-width="1.3"><circle cx="9" cy="9" r="6.5"/><ellipse cx="9" cy="9" rx="3" ry="6.5"/><path d="M2.5,9 H15.5"/></svg>
      </span>
      www.rwofficepartners.com.au
    </li>
  </ul>
  <div class="social-row">
    <span class="social-item"><span class="social-dot"></span>@rwofficepartners</span>
    <span class="social-item"><span class="social-dot"></span>@rwofficepartners</span>
  </div>
</section>

</body>
</html>
```